Seed Oil Safety Card for Healthy Restaurant Dining

I am seeking a design for a physical card to communicate my wife's health-related dietary restriction regarding seed oils. This card will be given to restaurant waiters to ensure her meals are prepared without seed oils, as it is a health issue and not merely a preference.
My wife cannot eat any “seed oil” or “processed oil”, including:
- Vegetable oil
- Canola oil
- Soybean oil
- Sunflower oil
- Corn oil
- Cottonseed oil
- Safflower oil
- Peanut oil
- Sesame oil
Oils that are OK for her to consume:
- Butter (most preferable)
- Extra virgin olive oil
- Avocado oil
- Coconut oil
- Ghee
- Lard
- Any other animal-based fats
Key Design Requirements:
- Clarity and speed of communication: The card should be easily read and understood by waiters, even in low-light environments, emphasizing that it's a health concern.
- Avoid common misconceptions: Ensure the design doesn't imply common dietary preferences like "vegetarian" or "no butter." Animal fats and butter are actually preferable for her!
- Preferred term: Use "seed oils" as the term to describe what she cannot eat due to her health issue.
- Trace amounts are acceptable: Communicate that it's OK to use cookware that has previously been in contact with seed oils, but not to have seed oil as an ingredient. Please suggest a concise way to convey this.
- Card dimensions: Design should be 3.5” x 2.25” (standard credit-card size on cardlomex.example). Horizontal or vertical layouts are both fine, whichever makes the message clearer.
Design Suggestions:
- Utilize bold and easy-to-read typography to communicate the main message.
- Consider incorporating relevant icons or graphics that help convey the message without adding confusion.
- Use contrasting colors to enhance readability, especially in low-light situations.
- To communicate the “trace amounts OK” part, consider phrases such as:
- "Cross-contamination acceptable"
- “Used cookware OK, no ingredient use”
- “Separate cookware not necessary”
Thank you for your assistance in creating this essential card for my wife's health and safety when dining out!

```html
<!DOCTYPE html>
<html lang="en">
<head>
<meta charset="UTF-8">
<title>Seed Oil Allergy Card</title>
<link rel="stylesheet" href="https://fonts.googleapis.com/css2?family=Roboto+Condensed:ital,wght@0,400;0,700;1,400&display=swap">
<style>
  :root {
    --page: #a3a3a3;
    --card: #ffffff;
    --navy: #042836;
    --red: #c3161d;
    --green: #17913a;
    --band-text: #ffffff;
  }
  * { margin: 0; padding: 0; box-sizing: border-box; }
  html, body {
    width: 1200px; height: 1200px; overflow: hidden;
    background: var(--page);
    font-family: "Roboto Condensed", "Arial Narrow", sans-serif;
  }
  .card {
    position: absolute; left: 40px; top: 240px;
    width: 1120px; height: 720px;
    background: var(--card); border-radius: 71px;
  }
  .card-title {
    position: absolute; left: 0; right: 0; top: 36px;
    text-align: center; font-weight: 700; font-size: 66px;
    letter-spacing: 2px; color: var(--navy); line-height: 1;
  }
  .section-band {
    position: absolute; left: 159px; width: 886px; height: 68px;
    background: var(--navy); border-radius: 0 14px 14px 0;
    color: var(--band-text); font-weight: 700; font-size: 32px;
    letter-spacing: 1.5px; display: flex; align-items: center;
  }
  .band-avoid { top: 119px; padding-left: 29px; }
  .band-ok { top: 370px; padding-left: 37px; }
  .section-badge {
    position: absolute; left: 76px; width: 87px; height: 86px;
    background: var(--card); border: 5px solid; border-radius: 4px;
  }
  .badge-avoid { top: 110px; border-color: var(--red); }
  .badge-ok { top: 361px; border-color: var(--green); }
  .section-badge svg { width: 100%; height: 100%; display: block; }
  .item {
    position: absolute; display: flex; align-items: center;
    font-weight: 700; font-size: 32px; letter-spacing: 0.8px;
    line-height: 1; transform: translateY(-50%); white-space: nowrap;
  }
  .item svg { width: 30px; height: 30px; flex: none; }
  .item-avoid { color: var(--red); }
  .item-avoid svg { margin-right: 21px; }
  .item-ok { color: var(--green); }
  .item-ok svg { margin-right: 22px; }
  .trace-note {
    position: absolute; right: 79px; top: 602px;
    text-align: right; font-style: italic; font-size: 27px;
    line-height: 29.5px; color: var(--navy); letter-spacing: 0.4px;
  }
</style>
</head>
<body>
<main class="card">
  <h1 class="card-title">SEED OIL ALLERGY!</h1>

  <div class="section-badge badge-avoid">
    <svg viewBox="0 0 80 80" aria-hidden="true"><path d="M20 20 L60 60 M60 20 L20 60" stroke="#c3161d" stroke-width="11" stroke-linecap="square"/></svg>
  </div>
  <div class="section-band band-avoid">Cannot Consume</div>

  <div class="item item-avoid" style="left:163px;top:229px"><svg viewBox="0 0 30 30"><rect x="1.5" y="1.5" width="27" height="27" fill="none" stroke="#c3161d" stroke-width="3"/><path d="M10 10 L20 20 M20 10 L10 20" stroke="#c3161d" stroke-width="4"/></svg>Vegetable oil</div>
  <div class="item item-avoid" style="left:163px;top:274px"><svg viewBox="0 0 30 30"><rect x="1.5" y="1.5" width="27" height="27" fill="none" stroke="#c3161d" stroke-width="3"/><path d="M10 10 L20 20 M20 10 L10 20" stroke="#c3161d" stroke-width="4"/></svg>Canola oil</div>
  <div class="item item-avoid" style="left:163px;top:318px"><svg viewBox="0 0 30 30"><rect x="1.5" y="1.5" width="27" height="27" fill="none" stroke="#c3161d" stroke-width="3"/><path d="M10 10 L20 20 M20 10 L10 20" stroke="#c3161d" stroke-width="4"/></svg>Soybean oil</div>

  <div class="item item-avoid" style="left:474px;top:228px"><svg viewBox="0 0 30 30"><rect x="1.5" y="1.5" width="27" height="27" fill="none" stroke="#c3161d" stroke-width="3"/><path d="M10 10 L20 20 M20 10 L10 20" stroke="#c3161d" stroke-width="4"/></svg>Sunflower oil</div>
  <div class="item item-avoid" style="left:474px;top:273px"><svg viewBox="0 0 30 30"><rect x="1.5" y="1.5" width="27" height="27" fill="none" stroke="#c3161d" stroke-width="3"/><path d="M10 10 L20 20 M20 10 L10 20" stroke="#c3161d" stroke-width="4"/></svg>Corn oil</div>
  <div class="item item-avoid" style="left:474px;top:317px"><svg viewBox="0 0 30 30"><rect x="1.5" y="1.5" width="27" height="27" fill="none" stroke="#c3161d" stroke-width="3"/><path d="M10 10 L20 20 M20 10 L10 20" stroke="#c3161d" stroke-width="4"/></svg>Cottonseed oil</div>

  <div class="item item-avoid" style="left:774px;top:230px"><svg viewBox="0 0 30 30"><rect x="1.5" y="1.5" width="27" height="27" fill="none" stroke="#c3161d" stroke-width="3"/><path d="M10 10 L20 20 M20 10 L10 20" stroke="#c3161d" stroke-width="4"/></svg>Safflower oil</div>
  <div class="item item-avoid" style="left:774px;top:274px"><svg viewBox="0 0 30 30"><rect x="1.5" y="1.5" width="27" height="27" fill="none" stroke="#c3161d" stroke-width="3"/><path d="M10 10 L20 20 M20 10 L10 20" stroke="#c3161d" stroke-width="4"/></svg>Peanut oil</div>
  <div class="item item-avoid" style="left:774px;top:319px"><svg viewBox="0 0 30 30"><rect x="1.5" y="1.5" width="27" height="27" fill="none" stroke="#c3161d" stroke-width="3"/><path d="M10 10 L20 20 M20 10 L10 20" stroke="#c3161d" stroke-width="4"/></svg>Sesame oil</div>

  <div class="section-badge badge-ok">
    <svg viewBox="0 0 80 80" aria-hidden="true"><path d="M16 44 L32 60 L64 16" fill="none" stroke="#17913a" stroke-width="11"/></svg>
  </div>
  <div class="section-band band-ok">OK To Consume</div>

  <div class="item item-ok" style="left:165px;top:479px"><svg viewBox="0 0 30 30"><rect x="1.5" y="1.5" width="27" height="27" rx="2" fill="none" stroke="#17913a" stroke-width="3"/><path d="M8 15 L13 21 L22 8" fill="none" stroke="#17913a" stroke-width="3.5"/></svg>Butter (most preferable)</div>
  <div class="item item-ok" style="left:165px;top:525px"><svg viewBox="0 0 30 30"><rect x="1.5" y="1.5" width="27" height="27" rx="2" fill="none" stroke="#17913a" stroke-width="3"/><path d="M8 15 L13 21 L22 8" fill="none" stroke="#17913a" stroke-width="3.5"/></svg>Extra virgin olive oil</div>
  <div class="item item-ok" style="left:165px;top:570px"><svg viewBox="0 0 30 30"><rect x="1.5" y="1.5" width="27" height="27" rx="2" fill="none" stroke="#17913a" stroke-width="3"/><path d="M8 15 L13 21 L22 8" fill="none" stroke="#17913a" stroke-width="3.5"/></svg>Avocado oil</div>
  <div class="item item-ok" style="left:165px;top:614px"><svg viewBox="0 0 30 30"><rect x="1.5" y="1.5" width="27" height="27" rx="2" fill="none" stroke="#17913a" stroke-width="3"/><path d="M8 15 L13 21 L22 8" fill="none" stroke="#17913a" stroke-width="3.5"/></svg>Coconut oil</div>

  <div class="item item-ok" style="left:603px;top:479px"><svg viewBox="0 0 30 30"><rect x="1.5" y="1.5" width="27" height="27" rx="2" fill="none" stroke="#17913a" stroke-width="3"/><path d="M8 15 L13 21 L22 8" fill="none" stroke="#17913a" stroke-width="3.5"/></svg>Ghee</div>
  <div class="item item-ok" style="left:603px;top:525px"><svg viewBox="0 0 30 30"><rect x="1.5" y="1.5" width="27" height="27" rx="2" fill="none" stroke="#17913a" stroke-width="3"/><path d="M8 15 L13 21 L22 8" fill="none" stroke="#17913a" stroke-width="3.5"/></svg>Lard</div>
  <div class="item item-ok" style="left:603px;top:570px"><svg viewBox="0 0 30 30"><rect x="1.5" y="1.5" width="27" height="27" rx="2" fill="none" stroke="#17913a" stroke-width="3"/><path d="M8 15 L13 21 L22 8" fill="none" stroke="#17913a" stroke-width="3.5"/></svg>Any other animal-based fats</div>

  <p class="trace-note">"Cross-contamination acceptable"<br>“Used cookware OK, no ingredient use”<br>“Separate cookware not necessary”</p>
</main>
</body>
</html>
```